BRAMLEIGH real estate family office

Hello, Our business is a real estate intermediation activity on high-end goods (amounts exceeding € 10m) for corporate and private clients. You can see our logo on the site www.bramleigh-invented.fr We would like to keep that spirit with the hexagon that represents France (transactions between Monaco and Saint Tropez, Courchevel and Paris). And the "baseline" that is "real estate family office". The corporate logo should be and can be printed by embossing (relief). We must integrate the name, first name, phone, email and website. Finally, to imbibe the spirit of business, here is a detail of the activity. "Genuine consulting firm in real estate investments, BRAMLEIGH works with its customers as a specialized player in the high-end markets, we are recognized for our ultra-confidential approach and tailor-made, as well as the quality of our network. We broadcast any information on the market and we work exclusively through a strong relationship we have developed over the years. BRAMLEIGH is active on the French Riviera (from Monaco to Saint-Tropez), the Alps (Courchevel, Méribel, Megève) and Paris (essentially market premium). Always looking for opportunities for our clients, we work on two investment areas: residential luxury real estate (properties, vineyards, mansions, land, etc.) commercial real estate (empty office buildings or yield, hotel properties, land, etc.) "

Target Market(s)

High foreign end customers. corporate and private.

Industry/Entity Type

Real Estate

Contact Information for Business Card

LOGO
baseline
Laurent Dufossé
+33(0)6.41.57.09.64
ld@bramleigh-invented.fr
www.bramleigh-invented.fr

Font styles to use
Serif

Colors
cedeed
0255a3
3277b5
85abd2
85cae6
34a7d7
0792cd
cfdeed
1b1b1b

Requirements
Must have
• see description

```html
<!DOCTYPE html>
<html lang="en">
<head>
<meta charset="utf-8">
<title>BRAMLEIGH – Business Card</title>
<link rel="stylesheet" href="https://fonts.googleapis.com/css2?family=Didact+Gothic&display=swap">
<style>
  :root {
    --backdrop: #e4e6e9;
    --card: #f4f2ee;
    --ink-grey: #6f7276;
    --ink-blue: #0a3fa0;
    --ink-dark: #3a3a3a;
    --rule: #8a8d90;
  }
  * { box-sizing: border-box; margin: 0; padding: 0; }
  html, body {
    width: 909px;
    height: 1200px;
    overflow: hidden;
    background: var(--backdrop);
    font-family: "Didact Gothic", "Century Gothic", sans-serif;
  }
  .sheet {
    width: 909px;
    height: 1200px;
    display: flex;
    flex-direction: column;
    align-items: center;
    justify-content: center;
    gap: 90px;
  }
  .card {
    width: 680px;
    height: 390px;
    background: var(--card);
    box-shadow: 0 10px 28px rgba(0,0,0,0.18);
    position: relative;
    display: flex;
    align-items: center;
    justify-content: center;
  }

  /* Front */
  .brand {
    display: flex;
    flex-direction: column;
    align-items: flex-end;
  }
  .brand-name {
    font-size: 58px;
    letter-spacing: 4px;
    color: var(--ink-grey);
    line-height: 1;
  }
  .brand-baseline {
    font-size: 19px;
    letter-spacing: 1.5px;
    color: var(--ink-blue);
    margin-top: 6px;
  }

  /* Back */
  .card-back { justify-content: flex-start; padding-left: 150px; }
  .back-mark {
    width: 62px;
    height: 62px;
    border: 5px solid var(--ink-grey);
  }
  .divider {
    width: 1.5px;
    height: 118px;
    background: var(--rule);
    margin: 0 36px 0 50px;
  }
  .contact-name {
    font-size: 27px;
    color: var(--ink-blue);
    margin-bottom: 10px;
  }
  .contact-list { list-style: none; }
  .contact-list li {
    display: flex;
    align-items: center;
    gap: 10px;
    font-size: 17px;
    color: var(--ink-dark);
    line-height: 1.55;
  }
  .contact-list svg { width: 15px; height: 15px; flex: none; }
  .contact-list svg * { fill: var(--ink-blue); }
</style>
</head>
<body>
<main class="sheet">
  <section class="card card-front">
    <div class="brand">
      <div class="brand-name">BRAMLEIGH</div>
      <div class="brand-baseline">real estate family office</div>
    </div>
  </section>

  <section class="card card-back">
    <div class="back-mark"></div>
    <div class="divider"></div>
    <div class="contact">
      <div class="contact-name">Laurent Dufossé</div>
      <ul class="contact-list">
        <li>
          <svg viewBox="0 0 16 16" aria-hidden="true"><path d="M4 1 L6.5 4 L5 5.8 C6 8 8 10 10.2 11 L12 9.5 L15 12 L13 14.5 C7 14 2 9 1.5 3 Z"/></svg>
          +33(0)6.41.57.09.64
        </li>
        <li>
          <svg viewBox="0 0 16 16" aria-hidden="true"><path d="M1 3 H15 V13 H1 Z M2 4 L8 9 L14 4 Z" fill-rule="evenodd"/></svg>
          ld@bramleigh-invented.fr
        </li>
        <li>
          <svg viewBox="0 0 16 16" aria-hidden="true"><circle cx="8" cy="8" r="7"/></svg>
          www.bramleigh-invented.fr
        </li>
      </ul>
    </div>
  </section>
</main>
</body>
</html>
```